If everything digital fails, here's what to do

Hi, I would like a poster / infographic of a list of practical actions people could take in case the internet stops working. I've put together a list of 8 areas, with the situation for each, and the mitigation actions folks can take - I need it presented in a clear and aesthetically pleasing way. I will send you the file with the full text so you can include it all

Target Market(s)

General population, but likely people who are safety conscious and want to protect themselves and learn more about what to do to be tech literate and prepared

Industry/Entity Type

Tech / Cyber / Public safety / Civic tech

Font styles to use
Sans Serif

Requirements
Must have
• It's a lot of text, so I think the important thing is to have it all in one poster, or in a series of similar pages
Nice to have
• I would like it to be a bit brooding, but also elicit competence and that some experts have thought about this and it will all be okay
Should not have
• I don't want it to look cartoonish, or cheap - less is more is sort of what I'm looking for

```html
<!DOCTYPE html>
<html lang="en">
<head>
<meta charset="utf-8">
<title>If Everything Digital Fails – Here's What To Do</title>
<link href="https://fonts.googleapis.com/css2?family=Bebas+Neue&family=Poppins:ital,wght@0,400;0,600;0,700;0,800;1,400&display=swap" rel="stylesheet">
<style>
  :root{
    --navy-deep:#0d1b45;
    --navy-card:#14305f;
    --navy-card-2:#1a3c6e;
    --sky:#4fc6f5;
    --ink-blue:#1a6aa6;
    --ink-dark:#17457a;
    --line:rgba(150,190,235,.75);
    --white:#ffffff;
    --note:#e6eef8;
    --amber:#ffc20e;
    --amber-ink:#1a1a2e;
  }
  *{box-sizing:border-box;margin:0;padding:0}
  html,body{width:816px;height:1200px;overflow:hidden}
  body{background:var(--navy-deep);font-family:'Poppins',sans-serif;color:var(--white)}
  .poster{position:relative;width:816px;height:1200px;overflow:hidden;
    background:linear-gradient(180deg,#163a80 0%,#14306e 30%,#112a5e 60%,var(--navy-deep) 100%)}
  .poster__backdrop{position:absolute;left:0;top:0;width:816px;height:600px;
    background:radial-gradient(ellipse 60% 55% at 50% 28%,#1f4f9f 0%,rgba(30,76,156,.5) 45%,rgba(22,58,128,0) 100%)}
  .masthead{position:absolute;top:44px;left:0;width:100%;text-align:center}
  .masthead__title{font-family:'Bebas Neue',sans-serif;font-weight:400;color:var(--sky);font-size:54px;line-height:.86;letter-spacing:.5px}
  .masthead__sub{font-family:'Bebas Neue',sans-serif;font-weight:400;color:var(--white);font-size:42px;line-height:1;margin-top:8px;letter-spacing:.3px}
  .masthead__date{display:inline-block;margin-top:22px;background:var(--amber);color:var(--amber-ink);font-family:'Bebas Neue',sans-serif;font-size:17px;letter-spacing:.2px;padding:7px 24px 5px;border-radius:18px}

  .card{position:absolute;display:flex;flex-direction:column;
    clip-path:polygon(0 0,calc(100% - 10px) 0,100% 10px,100% 100%,12px 100%,0 calc(100% - 12px))}
  .card__head{position:relative;background:var(--white);padding:14px 8px 10px 16px;height:102px;flex:none}
  .card__num{font-family:'Poppins',sans-serif;font-weight:800;color:var(--ink-blue);font-size:25px;line-height:1}
  .card__title{font-family:'Bebas Neue',sans-serif;font-weight:400;color:var(--ink-dark);font-size:18.5px;line-height:.95;margin-top:6px;letter-spacing:.2px}
  .card__situation{font-weight:600;color:var(--ink-blue);font-size:8.4px;line-height:1.1;margin-top:3px}
  .card__icon{position:absolute;top:8px;right:14px;width:26px;height:26px}
  .card__body{flex:1;background:linear-gradient(180deg,var(--navy-card) 0%,var(--navy-card-2) 100%);
    border:1px solid var(--line);border-top:none;padding:10px 8px 10px 6px}
  .actions{list-style:none}
  .action{position:relative;padding-left:15px;margin-bottom:9px}
  .action::before{content:"";position:absolute;left:0;top:0;width:9px;height:9px;border:1px solid var(--white);border-radius:50%}
  .action::after{content:"";position:absolute;left:3px;top:2px;width:2.4px;height:4px;border:solid var(--white);border-width:0 1px 1px 0;transform:rotate(45deg)}
  .action__do{font-weight:700;font-size:7.9px;line-height:1.25}
  .action__refresh{font-style:italic;color:var(--sky);font-size:6.7px;line-height:1.22;margin-top:3px}
  .action__note{color:var(--note);font-size:6.6px;line-height:1.2;margin-top:5px}

  .card--split{flex-direction:row;
    clip-path:polygon(0 0,100% 0,100% 100%,12px 100%,0 calc(100% - 12px))}
  .card--split .card__head{width:190px;height:auto;display:flex;flex-direction:column;justify-content:center;padding:38px 12px 10px 20px}
  .card--split .card__body{border-top:1px solid var(--line);border-left:none;padding:12px 10px 8px 8px;
    clip-path:polygon(0 0,calc(100% - 10px) 0,100% 10px,100% 100%,0 100%)}
  .card--split .action__do{font-size:7.6px;line-height:1.22}
</style>
</head>
<body>
<main class="poster">
  <div class="poster__backdrop" role="img" aria-label="Abstract glowing tech tunnel backdrop behind the title"></div>

  <header class="masthead">
    <h1 class="masthead__title">If Everything<br>Digital Fails</h1>
    <p class="masthead__sub">Here’s What To Do – A List</p>
    <p class="masthead__date">(Last Updated: April 2023)</p>
  </header>

  <article class="card" style="left:13px;top:329px;width:192px;height:618px">
    <div class="card__head">
      <svg class="card__icon" viewBox="0 0 24 24" fill="none" stroke="#1a6aa6" stroke-width="1.1"><rect x="7" y="2" width="15" height="10" rx="1"/><path d="M10 5h9M10 8h7"/><path d="M2 10h11v8H6l-3 3v-3H2z"/><path d="M4 13h7M4 15h5"/></svg>
      <div class="card__num">1.</div>
      <h2 class="card__title">Communications</h2>
      <p class="card__situation">Cell phones / land-line phone services have stopped working</p>
    </div>
    <div class="card__body">
      <ul class="actions">
        <li class="action"><p class="action__do">Buy a two-way hand-held walkie talkie and share the other with close friends.</p>
          <p class="action__refresh">Refresh when? Check to ensure your walkie talkie has working batteries every 12 months (and that you know / remember how the walkie talkie itself works)</p></li>
        <li class="action"><p class="action__do">Share a ‘third space’ safe spot with close contacts in town where you know you could meet in emergency situations if your home was not safe to remain in. Do the same with neighbours and folks who live in your neighbourhood – have a central gathering spot in your hood that you share with others so you can have a convening spot close by.</p>
          <p class="action__refresh">Refresh when? Have a quick reminder conversation about this with your close contacts every 12 months to ensure everyone knows that’s the plan</p></li>
        <li class="action"><p class="action__do">Have a printed list of your close contacts’ home addresses handy, if you don’t know how to get to their places by heart.</p>
          <p class="action__refresh">Refresh when? Print a new such document every 12 months to ensure it stays up to date</p></li>
        <li class="action"><p class="action__do">Have a list of close contacts that might still have a working landline (ie. rotary, not voip-based), or who have a satellite phone</p>
          <p class="action__refresh">Refresh when? Remind yourself of this list and refresh it every 12 months or so</p></li>
        <li class="action"><p class="action__do">Make a list of the people in your life that you care about that may also be affected, and make sure you include individuals in your community that may be vulnerable in such a disruption (they may be older, may live alone, might need access to supply of medication).</p>
          <p class="action__refresh">Refresh when? Remind yourself of this list and refresh it every 12 months or so</p></li>
      </ul>
    </div>
  </article>

  <article class="card" style="left:212px;top:329px;width:192px;height:336px">
    <div class="card__head">
      <svg class="card__icon" viewBox="0 0 24 24" fill="none" stroke="#1a6aa6" stroke-width="1.1"><path d="M2 9l9-6 2 1-5 5 3 1 2-2 1 1-2 4"/><circle cx="19" cy="5" r="3"/><path d="M6 15h9v5H6zM15 16h3l2 2v2h-5"/><circle cx="8" cy="21" r="1"/><circle cx="17" cy="21" r="1"/></svg>
      <div class="card__num">2.</div>
      <h2 class="card__title">Transportation</h2>
      <p class="card__situation">Gas stations have stopped working</p>
    </div>
    <div class="card__body">
      <ul class="actions">
        <li class="action"><p class="action__do">(If you own a car) Have a standard 40L gas canister filled with gas and available close by in case needed.</p>
          <p class="action__refresh">Refresh when? Use up the gas within 4 months or so, and refill the canister then (i.e. 3 times a year) so that it remains usable</p>
          <p class="action__note">Safety note: (If relevant) ensure the can is not in a place where kids can get to it, since it’s not safe for kids to be around gas</p></li>
      </ul>
    </div>
  </article>

  <article class="card" style="left:410px;top:329px;width:192px;height:336px">
    <div class="card__head">
      <svg class="card__icon" viewBox="0 0 24 24" fill="none" stroke="#1a6aa6" stroke-width="1.1"><rect x="4" y="2" width="13" height="18"/><path d="M7 6h7M7 9h7M7 12h7M7 15h5"/><circle cx="20" cy="11" r="2.5"/></svg>
      <div class="card__num">3.</div>
      <h2 class="card__title">Information Management</h2>
      <p class="card__situation">Cloud storage services have stopped working</p>
    </div>
    <div class="card__body">
      <ul class="actions">
        <li class="action"><p class="action__do">Do a backup of the important documents that are stored only in your cloud storage (e.g. that important email in your Mailbox inbox; that tax document only issued digitally, etc.)</p>
          <p class="action__refresh">Refresh when? Do a backup and update every 6 months</p>
          <p class="action__note">Note: Since this is a time-consuming exercise but not necessarily the same exercise as #7 below, you could alternate the months when you do one versus the other. For example, you could do this with annual equinoxes: March 21 and Sept 21 (pro tip: star email messages that are important as they arrive, so that you know what needs to be backed up every six months; that way, you don’t have to go searching through your whole inbox)</p></li>
      </ul>
    </div>
  </article>

  <article class="card" style="left:608px;top:329px;width:192px;height:618px">
    <div class="card__head">
      <svg class="card__icon" viewBox="0 0 24 24" fill="none" stroke="#1a6aa6" stroke-width="1.1"><rect x="3" y="2" width="10" height="20" rx="1.5"/><rect x="11" y="7" width="9" height="9"/><path d="M13 5v2M16 5v2M18 5v2M13 16v2M16 16v2M18 16v2M20 9h2M20 12h2M20 14h2"/><path d="M5 6h3M5 9h3M5 12h3"/></svg>
      <div class="card__num">4.</div>
      <h2 class="card__title">Technology</h2>
      <p class="card__situation">Computers (laptops, tablets, smart phones) have stopped working</p>
    </div>
    <div class="card__body">
      <ul class="actions">
        <li class="action"><p class="action__do">Save all important digital materials (e.g. photos) that don’t also exist on paper on a portable hard drive. Remember to do this for all digital materials that have been saved to your cloud that you might have forgotten about (archived, etc.).</p>
          <p class="action__refresh">Refresh when? Do a backup and update every 6 months</p>
          <p class="action__note">Note: Since this is time-consuming, put a note in your calendar at the beginning of the year, choosing the time and date when you will do this (as noted in #5 above, you could do this in line with the solstice each year: June 20 and December 20)</p></li>
        <li class="action"><p class="action__do">Get a hand cranked radio to ensure you have access to important news and information about what’s happening in your community (locally, as well as nationally/ internationally).</p>
          <p class="action__refresh">Refresh when? Make sure the hand cranked radio has fresh batteries (change them every 12 months or so)</p></li>
        <li class="action"><p class="action__do">Download a copy of your city’s maps (e.g. Waymark Maps) on your phone for local access, and make sure you have a physical map in case you need to get somewhere new in your city in a rush, and you don’t know how to get there.</p>
          <p class="action__refresh">Refresh when: N/A once done</p></li>
      </ul>
    </div>
  </article>

  <article class="card" style="left:212px;top:677px;width:192px;height:270px">
    <div class="card__head">
      <svg class="card__icon" viewBox="0 0 24 24" fill="none" stroke="#1a6aa6" stroke-width="1.1"><rect x="3" y="2" width="10" height="20" rx="1.5"/><rect x="11" y="7" width="9" height="9"/><path d="M13 5v2M16 5v2M18 5v2M13 16v2M16 16v2M18 16v2M20 9h2M20 12h2"/></svg>
      <div class="card__num">5.</div>
      <h2 class="card__title">Information Management</h2>
      <p class="card__situation">Password manager services (cloud) have stopped working</p>
    </div>
    <div class="card__body">
      <ul class="actions">
        <li class="action"><p class="action__do">Preamble: Many individuals don’t remember their passwords anymore, having password managers generate complicated strings of characters as their passwords for their many digital accounts in their lives. Print a full list of your accounts and their passwords and keep that document safely in your living space.</p>
          <p class="action__refresh">Refresh when? Print a new such document every 6 months to ensure the list remains up to date</p></li>
      </ul>
    </div>
  </article>

  <article class="card" style="left:410px;top:677px;width:192px;height:270px">
    <div class="card__head">
      <svg class="card__icon" viewBox="0 0 24 24" fill="none" stroke="#1a6aa6" stroke-width="1.1"><path d="M2 8l10-5 10 5zM3 9h18M3 20h18M2 22h20"/><path d="M5 10v9M9 10v9M12 10v9M15 10v9M19 10v9"/></svg>
      <div class="card__num">6.</div>
      <h2 class="card__title">Banking</h2>
      <p class="card__situation">Debit and credit cards have stopped working (in stores; ATMs)</p>
    </div>
    <div class="card__body">
      <ul class="actions">
        <li class="action"><p class="action__do">Have $500 in cash available in $20 bills.</p>
          <p class="action__refresh">Refresh when? N/A once done</p></li>
      </ul>
    </div>
  </article>

  <article class="card card--split" style="left:13px;top:960px;width:391px;height:197px">
    <div class="card__head">
      <svg class="card__icon" viewBox="0 0 24 24" fill="none" stroke="#1a6aa6" stroke-width="1.1"><rect x="8" y="2" width="14" height="14" rx="1"/><path d="M8 5h14M11 9h4M11 12h4M19 8v6"/><circle cx="6" cy="13" r="2.5"/><path d="M1.5 22v-2.5a4.5 4.5 0 0 1 9 0V22z"/></svg>
      <div class="card__num">7.</div>
      <h2 class="card__title">Banking</h2>
      <p class="card__situation">Debit and credit cards have stopped working; your bank can’t access its own information (online)</p>
    </div>
    <div class="card__body">
      <ul class="actions">
        <li class="action"><p class="action__do">Print paper records of your banking statements that prove what you have in your bank accounts and store it in a safe place in your living space. Ensure it has dates showing and full amounts, as well as your identifiers (name and account numbers) as well as the institution itself (printed screenshots should work fine if your money is in a few accounts requiring many statements). Note the same goes for your liabilities (i.e. be able to prove how much you had left on your mortgage or other bigger loans, if you have such debt).</p>
          <p class="action__refresh">Refresh when? Update this document every 6-12 months</p></li>
      </ul>
    </div>
  </article>

  <article class="card card--split" style="left:410px;top:960px;width:390px;height:197px">
    <div class="card__head">
      <svg class="card__icon" viewBox="0 0 24 24" fill="none" stroke="#1a6aa6" stroke-width="1.1"><rect x="3" y="5" width="18" height="15" rx="1"/><path d="M8 5V3h8v2"/><circle cx="12" cy="12.5" r="3.2"/><path d="M12 8v1.3M12 15.7V17M7.5 12.5h1.3M15.2 12.5h1.3"/></svg>
      <div class="card__num">8.</div>
      <h2 class="card__title">Information<br>Management</h2>
      <p class="card__situation">Cloud storage services have stopped working</p>
    </div>
    <div class="card__body">
      <ul class="actions">
        <li class="action"><p class="action__do">Print paper records of your banking statements that prove what you have in your bank accounts and store it in a safe place in your living space. Ensure it has dates showing and full amounts, as well as your identifiers (name and account numbers) as well as the institution itself (printed screenshots should work fine if your money is in a few accounts requiring many statements). Note the same goes for your liabilities (i.e. be able to prove how much you had left on your mortgage or other bigger loans, if you have such debt).</p>
          <p class="action__refresh">Refresh when? Update this document every 6-12 months</p></li>
      </ul>
    </div>
  </article>
</main>
</body>
</html>
```